Etiketten-Design für Rotwein Wild Saison 2018
Zielgruppe
Wir sind ein Getränke Fachgroßhändler im Norden und möchten eine kreatives Etikett unter dem wir unsere Moor Tropf Eigenmarke vermarkte können.
Zielgruppe Gastronomie / Restaurant und Hotels
Aufgabenstellung
Rotwein für die Wild Saison 2018
Wir benötigen ein Vorderetikett (Rückenetikett vorhanden)
Maße 80mm x 80 mm
Wir hätten gerne ein Etikett welches bunt, kreativ, innovativ und trinkanimierend ist.
Der Name MOORTROPF sollte auf dem Etikett stehen – es kann auch ein anderer Begriff genommen werden der den Zusammenhang zum Moor Tropf wiederspiegelt.
Es wird eine feinherbe Cuvée aus Cabernet Sauvignon & Spätburgunder.
Die Rebsorten und das Wort feinherb müssen nicht zwangsläufig auf dem Etikett erscheinen.

```html
<!DOCTYPE html>
<html lang="de">
<head>
<meta charset="utf-8">
<title>MoorTropf feinherb – Vorderetikett</title>
<link rel="stylesheet" href="https://fonts.googleapis.com/css2?family=Sofia+Sans+Extra+Condensed:wght@200&family=Advent+Pro:wght@400&display=swap">
<style>
  :root {
    --page: #ffffff;
    --ink-night: #050307;
    --teal: #1fb3a0;
    --magenta: #e0219a;
    --violet: #6a2ad0;
    --lime: #e6f24a;
    --coral: #ff5a2c;
    --label-white: #f2f2f2;
    --berry: #8a1d5c;
  }
  html, body {
    margin: 0;
    padding: 0;
    width: 1200px;
    height: 865px;
    overflow: hidden;
    background: var(--page);
  }
  .canvas {
    position: relative;
    width: 1200px;
    height: 865px;
    background: var(--page);
  }
  .label {
    position: absolute;
    left: 0;
    top: 0;
    width: 864px;
    height: 865px;
    overflow: hidden;
    background: var(--ink-night);
  }
  .label__jungle {
    position: absolute;
    inset: 0;
    background:
      radial-gradient(circle at 62% 8%, var(--magenta) 0, transparent 22%),
      radial-gradient(circle at 90% 28%, var(--violet) 0, transparent 26%),
      radial-gradient(circle at 8% 22%, var(--lime) 0, transparent 14%),
      radial-gradient(circle at 20% 70%, var(--teal) 0, transparent 28%),
      radial-gradient(circle at 55% 62%, var(--teal) 0, transparent 22%),
      radial-gradient(circle at 78% 78%, var(--lime) 0, transparent 16%),
      radial-gradient(circle at 6% 40%, var(--coral) 0, transparent 10%),
      radial-gradient(circle at 40% 92%, var(--teal) 0, transparent 20%),
      var(--ink-night);
    opacity: 0.85;
  }
  .label__wordmark {
    position: absolute;
    left: 100px;
    top: 160px;
    height: 236px;
    margin: 0;
    padding: 0 26px;
    box-sizing: border-box;
    max-width: 700px;
    border-radius: 56px;
    background: var(--ink-night);
    color: var(--label-white);
    font-family: "Sofia Sans Extra Condensed", sans-serif;
    font-weight: 200;
    font-size: 228px;
    line-height: 236px;
    letter-spacing: 2px;
    white-space: nowrap;
  }
  .label__style {
    position: absolute;
    left: 330px;
    top: 406px;
    height: 84px;
    margin: 0;
    padding: 0 16px;
    box-sizing: border-box;
    border-radius: 28px;
    background: var(--ink-night);
    color: var(--berry);
    font-family: "Advent Pro", sans-serif;
    font-size: 68px;
    line-height: 80px;
    letter-spacing: 2px;
    white-space: nowrap;
  }
</style>
</head>
<body>
  <main class="canvas">
    <section class="label">
      <div class="label__jungle" role="img" aria-label="Bunte Dschungel-Illustration mit neonfarbenen Blättern, Ranken, Beeren und Blüten auf schwarzem Grund"></div>
      <h1 class="label__wordmark">MoorTropf</h1>
      <p class="label__style">feinherb</p>
    </section>
  </main>
</body>
</html>
```